Redesign Of Hotel Coupon/Voucher 8.5 x 11

I would like to redesign my voucher.

Please provide me a color flyer design but one that would be easy on printing costs...for example printing from home computer/printer.

I would like to see some color designs...maybe some black and white and also full graphics and even basic like the plum tally voucher I provided as a sample. The 2 night hotel stay is the voucher I need to redesign...

Target Market(s)

Consumers

Industry/Entity Type

Hotel

Requirements
Must have
• exact text in current designs---look official, credible and trust worthy
Nice to have
• I would like to redesign my voucher.
• Please provide me a color flyer design but one that would be easy on printing costs...for example printing from home computer/printer.
• I would like to see some color designs...maybe some black and white and also full graphics and even basic like the plum tally voucher I provided as a sample. The 2 night hotel stay is the voucher I need to redesign...
Should not have

```html
<!DOCTYPE html>
<html lang="en">
<head>
<meta charset="utf-8">
<title>2 Night Hotel Stay Certificate</title>
<link rel="stylesheet" href="https://fonts.googleapis.com/css2?family=Arimo:wght@400;700&family=Caveat:wght@400&family=PT+Sans+Narrow:wght@400;700&display=swap">
<style>
:root{
  --gold:#a88f45;
  --gold-band:#d8cfa4;
  --cream:#f1ebd3;
  --paper:#ffffff;
  --soft:#f2f2f2;
  --ink:#222222;
  --red:#d42a1f;
  --line:#333333;
}
*{box-sizing:border-box;margin:0;padding:0}
html,body{width:961px;height:1200px;overflow:hidden;background:#e9e9e9}
.voucher{position:relative;width:961px;height:1200px;background:var(--cream);font-family:"Arimo",Arial,sans-serif;color:var(--ink)}
.hero-photo{position:absolute;left:0;top:0;width:961px;height:378px;
  background:linear-gradient(180deg,#6f7f96 0%,#a7a6a5 22%,#8f8b86 40%,#5d5a57 58%,#3e3530 75%,#6b4b33 100%)}
.hero-title{position:absolute;left:34px;top:232px;font-family:"Caveat",cursive;font-size:104px;color:#fff;line-height:1;letter-spacing:1px}
.compliment-tag{position:absolute;left:729px;top:0;width:197px;height:208px}
.compliment-tag svg{position:absolute;inset:0}
.compliment-text{position:relative;text-align:center;padding-top:24px;font-size:17px;line-height:22px}
.compliment-text .who{margin-top:24px;font-weight:700;font-size:15.5px;line-height:17px}
.terms{position:absolute;left:0;top:378px;width:729px;height:427px;background:var(--soft);padding:12px 20px 0 20px}
.terms h2{font-family:"PT Sans Narrow",sans-serif;font-weight:400;color:var(--gold);font-size:26px;line-height:28px}
.terms p{font-family:"PT Sans Narrow",sans-serif;font-size:11.2px;line-height:13.6px;text-align:justify;margin-top:2px}
.band{position:absolute;left:0;top:805px;width:729px;height:7px;background:var(--gold-band)}
.destinations{position:absolute;left:729px;top:296px;width:197px;height:880px;background:var(--paper);padding:14px 0 0 11px;
  font-family:"PT Sans Narrow",sans-serif;color:var(--gold);font-size:14px;line-height:16.5px;list-style:none}
.card{position:absolute;background:var(--paper)}
.redeem{left:20px;top:732px;width:687px;height:91px;padding:8px 14px;font-family:"PT Sans Narrow",sans-serif;font-size:12.6px;line-height:14px}
.ways{display:flex;margin-top:6px;font-size:12px;line-height:13px}
.ways .lead{width:128px}
.ways .w1{width:210px;text-align:left}
.ways .w2{width:138px}
.ids{margin-top:8px;font-weight:700;font-size:12px}
.ids .val{color:var(--red);margin-right:12px}
.form-box{padding:12px 18px;font-size:13px}
.form-box h3{font-size:13.5px;font-weight:700;margin-bottom:8px}
.row{display:flex;align-items:flex-end;height:20.3px;font-weight:700}
.row .lab{width:60px}
.row .blank{flex:1;border-bottom:1px solid var(--line);height:12px}
.billing{left:20px;top:826px;width:311px;height:193px}
.shipping{left:20px;top:1029px;width:311px;height:150px}
.shipping h3{margin-bottom:4px}
.payment{left:342px;top:826px;width:365px;height:353px;padding:12px 20px}
.payment .sub{font-weight:700;margin-bottom:8px}
.methods{display:grid;grid-template-columns:82px 130px;margin-left:30px;row-gap:7px;font-weight:700;font-size:13.5px}
.methods span{display:flex;align-items:center;gap:6px}
.box{width:18px;height:17px;border:1px solid var(--line);display:inline-block}
.payment .row .lab{width:auto;margin-right:8px}
.exp .blank.s{flex:0 0 32px;margin-right:10px}
.exp .slash{margin-right:8px}
.exp .blank.l{flex:0 0 86px}
.cv .blank{flex:0 0 66px}
.agree{margin-top:18px}
.notes{margin-top:10px;font-weight:400;font-size:10px;line-height:16.6px}
.code{position:absolute;right:12px;bottom:4px;font-size:10px}
</style>
</head>
<body>
<main class="voucher">
  <div class="hero-photo" role="img" aria-label="Photo of a hotel suite lounge with a lamp and armchairs overlooking a city skyline at dusk"></div>
  <h1 class="hero-title">2 Night Hotel Stay</h1>

  <aside class="compliment-tag">
    <svg width="197" height="208" viewBox="0 0 197 208"><polygon points="0,0 197,0 197,172 98,208 0,172" fill="#fff"/></svg>
    <div class="compliment-text">THE CERTIFICATE IS<br>COMPLIMENT OF:
      <div class="who">NAME<br>PHONE NUMBER<br>E-MAIL ADDRESS</div>
    </div>
  </aside>

  <section class="terms">
    <h2>Terms &amp; Conditions</h2>
    <p>This certificate will be considered void if bartered or purchased for legal tender by the recipient. This certificate is valid for a reservation request form offering 2 adults 21 years of age and older plus up to 2 children under the age of 18, 2 nights of hotel accommodations in the city of their choice of available cities. The cost to activate this certificate to receive the reservation request form is just a one-time non-refundable $14.95 processing fee. The cost upon requesting reservations is just a tax &amp; fee deposit of $33 per night. Taxes &amp; fees usually range from $12-$33 per night depending on when and where you travel to. If the taxes &amp; fees are less than the $33 per night the difference will be refunded after travel is completed. 30 days advance reservation notice is required. In order to guarantee that you will show up to your booked reservation you will be required to pay a REFUNDABLE $50 “Reservation Guarantee Deposit”. If you send in your travel dates, etc and you do not end up traveling then the reservation guarantee deposit will not be refundable. 7 days before and after holidays and conventions are not available. This offer is valid 7 days a week subject to availability. Friday and Saturday nights will require a surcharge of $20 per night. A $5 per person per night surcharge is enforced for each child up to 2 children under the age of 18. This offer is not valid for group travel. The recipient of this certificate is responsible for all expenses including but not limited to: transfers, food, gratuities, all pertinent fees, taxes, hotel surcharges, resort fees and any other miscellaneous expenses. If you activate this certificate online you will be able to instantly print your reservation request form. If you cannot print your own reservation request form we will mail it to you. You should receive it in the mail within 14 days. This certificate cannot be combined with any other promotional vacation offer. The expiration date on this certificate pertains only to activation of this certificate and not actual travel. You must activate this certificate by th expiration date printed on this certificate in order to receive the reservation request form. You must fill out the reservation request form with your destination choices and arrival dates and mail it to our fulfillment department within 6 months after activation, however travel can be completed within 12 months after activation. You will be required to give the travel agency multiple arrival dates and destinations. Only one 2 Night Hotel certificate Per Household Per Year. This certificate has no cash surrender value, void if discontinued and where prohibited by law. The terms of this offer are subject to change without notice. Do not rely upon representations other than what is printed on this certificate or the reservation request form. CST # 2048613</p>
  </section>
  <div class="band"></div>

  <ul class="destinations">
    <li>Destinations Available:</li><li>Anaheim, CA</li><li>Atlanta, GA</li><li>Atlantic City, NJ</li><li>Branson, MO</li><li>Cancun, MX</li><li>Charleston, SC</li><li>Coeur d' Alene, ID</li><li>Daytona Beach, FL</li><li>Destin, FL</li><li>Ft. Lauderdale, FL</li><li>Ft. Meyers, FL</li><li>Gatlinburg, TN</li><li>Hilton Head, SC</li><li>Honolulu, HI</li><li>Kissimmee, FL</li><li>Lake Tahoe, CA</li><li>Las Vegas, NV</li><li>Myrtle Beach, SC</li><li>Niagara Falls/Buffalo Area, NY</li><li>Orlando, FL</li><li>Ormond Beach, FL</li><li>Palm Springs, CA</li><li>Pigeon Forge, TN</li><li>St. Petersburg, FL</li><li>San Antonio, TX</li><li>San Diego, CA</li><li>San Francisco, CA</li><li>Sedona, AZ</li><li>Sonoma Wine Country, CA</li><li>St. George, UT</li><li>Tampa, FL</li><li>Williamsburg, VA</li><li>Wisconsin Dells, WI</li><li>Tallahassee, FL</li><li>Augusta, GA</li><li>Columbia, SC</li><li>New York, NY</li><li>Florence, SC</li><li>Washington, D.C.</li><li>Chicago, IL</li><li>Salt Lake City, UT</li><li>Hollywood, CA</li><li>Dayton, OH</li><li>Tucson, AZ</li><li>Niagra Falls, ON/CAN</li><li>Seattle, WA</li><li>Portland, OR</li><li>Antioch, CA</li><li>San Mateo, CA</li><li>Brunswick, GA</li><li>Nashville, TN</li>
  </ul>

  <section class="card redeem">
    <div>Simply fill out the form on this certificate and enclose payment of U.S. $14.95. Vista Card, MeritCard, Atlas Express, Discovery Pay, Debit Card, Check Card, Check &amp; Money Orders are all accepted</div>
    <div class="ways">
      <div class="lead">3 Ways To Redeem:</div>
      <div class="w1">1. For expedited redemption go to:<br>&nbsp;&nbsp;&nbsp;&nbsp;www.StayVoucherHub.com</div>
      <div class="w2">2. Fax* certificate to:<br>&nbsp;&nbsp;&nbsp;&nbsp;1-888-555-0142</div>
      <div>3. Mail* to: Redemption Center<br>&nbsp;&nbsp;&nbsp;&nbsp;4120 Harbor View Rd Ste B #210<br>&nbsp;&nbsp;&nbsp;&nbsp;Bay Crest, Ca 90000</div>
    </div>
    <div class="ids" style="margin-top:-4px">Certificate ID: <span class="val">-10002</span> Expiration Date: <span class="val">04/08/2017</span></div>
  </section>

  <section class="card form-box billing">
    <h3>BILLING INFORMATION</h3>
    <div class="row"><span class="lab">Name:</span><span class="blank"></span></div>
    <div class="row"><span class="lab">Address:</span><span class="blank"></span></div>
    <div class="row"><span class="lab">City:</span><span class="blank"></span></div>
    <div class="row"><span class="lab">State:</span><span class="blank"></span></div>
    <div class="row"><span class="lab">Zip Code:</span><span class="blank"></span></div>
    <div class="row"><span class="lab">Country:</span><span class="blank"></span></div>
    <div class="row"><span class="lab">Phone:</span><span class="blank"></span></div>
    <div class="row"><span class="lab">Email:</span><span class="blank"></span></div>
  </section>

  <section class="card form-box shipping">
    <h3>SHIPPING INFORMATION</h3>
    <div class="row"><span class="lab">Name:</span><span class="blank"></span></div>
    <div class="row"><span class="lab">Address:</span><span class="blank"></span></div>
    <div class="row"><span class="lab">City:</span><span class="blank"></span></div>
    <div class="row"><span class="lab">State:</span><span class="blank"></span></div>
    <div class="row"><span class="lab">Zip Code:</span><span class="blank"></span></div>
    <div class="row"><span class="lab">Country:</span><span class="blank"></span></div>
  </section>

  <section class="card form-box payment">
    <h3>PAYMENT INFORMATION</h3>
    <div class="sub">Payment Method:</div>
    <div class="methods">
      <span><i class="box"></i>Check</span><span><i class="box"></i>Money Order</span>
      <span><i class="box"></i>Vista</span><span><i class="box"></i>MeritCard</span>
      <span><i class="box"></i>ATEX</span><span><i class="box"></i>Discovery Pay</span>
    </div>
    <div style="margin-top:6px">
      <div class="row"><span class="lab">Name On Card:</span><span class="blank" style="margin-left:30px"></span></div>
      <div class="row"><span class="lab">Card # (16 digits):</span><span class="blank"></span></div>
      <div class="row exp"><span class="lab">Expiration Date:</span><span class="blank s"></span><span class="slash">/</span><span class="blank l"></span></div>
      <div class="row cv"><span class="lab">CV2#**:</span><span class="blank"></span></div>
      <div class="row agree"><span class="lab">I agree to terms and conditions</span></div>
      <div class="row"><span class="lab">Signature:</span><span class="blank"></span></div>
    </div>
    <div class="notes">"Redemption Center" will appear on your billing statement.<br>Make checks and money orders payable to: "Redemption Center"<br>* You will receive your information by mail within 10 days.<br>** Last 3 digits on back of card (4 digits on front of Atlas Express).</div>
  </section>

  <div class="code">2NIL -10002</div>
</main>
</body>
</html>
```